Heavy Duty Repairs Poster

Good afternoon - I'm looking for a poster , design to set up around different areas. The Poster must consist of the following
- Heavy duty repairs
- Pictures of Semi trucks , heavy construction equipment , trailers
- Agriculture
- All north American equipment ( see attached pictures)
- Brief Descriptions in bullet point forms
CVIPS
WELDING
AIR CONDITIONING
ENGINE REBUILDS
DIAGONSTICS
FLEET MANAGMENT
TIRE REPAIR AND SALES
ELECTRICAL , HYDRALIC , POWER TRAIN SERVICE AND REPAIRS
PART SALES
FLEET MAINTINACE
DELTEING AND TUNING
AFTER MARKET INSTALLS OUTFITTING
ONSITE & OFFSITE REPAIRS
FULL RECERTIFACTION OVERHAULING
Warranty Approved

Target Market(s)

Heavy Duty Truck , Equipment , Agriculture Owners

Industry/Entity Type

Heavy Duty Repairs

Colors
EB3D1F
EC4F4E
F09395
F8D3D4
FCEDEE

Requirements
Must have
• Pictures of : Semi trucks and trailer , Construction heavy equipment , agriculture equipment
Nice to have
• Flashy and stands out

```html
<!DOCTYPE html>
<html lang="en">
<head>
<meta charset="utf-8">
<title>Heavy Duty Repairs Poster</title>
<link href="https://fonts.googleapis.com/css2?family=Oswald:wght@500;700&family=Russo+One&family=Roboto+Condensed:wght@700&display=swap" rel="stylesheet">
<style>
  :root {
    --red: #EB3D1F;
    --red-soft: #EC4F4E;
    --pink: #F09395;
    --blush: #F8D3D4;
    --mist: #FCEDEE;
    --ink: #111111;
    --charcoal: #1c1c1c;
    --paper: #eeeeee;
    --text: #222222;
  }
  * { box-sizing: border-box; margin: 0; padding: 0; }
  html, body { width: 849px; height: 1200px; overflow: hidden; background: #ffffff; }
  .poster {
    position: relative;
    width: 849px; height: 1200px;
    background: linear-gradient(180deg, #ffffff 0%, var(--paper) 45%, #dcdcdc 100%);
    font-family: "Roboto Condensed", Arial, sans-serif;
    overflow: hidden;
  }
  .header-stripes { position: absolute; left: 0; top: 0; width: 849px; height: 170px; }
  .brand {
    position: absolute; left: 0; right: 0; top: 46px;
    display: flex; justify-content: center; align-items: center; gap: 14px;
  }
  .brand-dot { width: 22px; height: 22px; border-radius: 50%; background: var(--red); }
  .brand-name {
    font-family: "Oswald", sans-serif; font-weight: 700;
    font-size: 40px; color: var(--ink); letter-spacing: 0.5px;
  }
  .hero-photo {
    position: absolute; left: 0; top: 150px; width: 849px; height: 400px;
    background: linear-gradient(180deg, #3d79c9 0%, #86b2e2 40%, #c9d3d9 60%, #8a8a86 72%, #6d6a63 100%);
  }
  .headline-band {
    position: absolute; left: 0; top: 550px; width: 849px; height: 78px;
    background: linear-gradient(180deg, #2a2a2a, #000000);
    border-top: 4px solid var(--red); border-bottom: 4px solid var(--red);
    display: flex; align-items: center; justify-content: center;
  }
  .headline {
    font-family: "Russo One", sans-serif; font-size: 54px; letter-spacing: 2px;
    background: linear-gradient(180deg, #ffffff 0%, #cfcfcf 50%, #8d8d8d 100%);
    -webkit-background-clip: text; background-clip: text; color: transparent;
  }
  .gallery {
    position: absolute; left: 80px; top: 648px; width: 689px; height: 150px;
    display: flex; justify-content: space-between;
  }
  .gallery-photo { width: 220px; height: 150px; border: 4px solid var(--red); }
  .photo-truck { background: linear-gradient(180deg, #5f8fcf 0%, #a8c3e0 45%, #6f6f6f 100%); }
  .photo-loader { background: linear-gradient(180deg, #6a8a4a 0%, #c9a53a 55%, #7a6a4a 100%); }
  .photo-tractor { background: linear-gradient(180deg, #b9c9dc 0%, #c0392b 55%, #6b4a34 100%); }
  .services-title {
    position: absolute; left: 0; right: 0; top: 810px; text-align: center;
    font-family: "Oswald", sans-serif; font-weight: 700; font-size: 40px; color: var(--red);
  }
  .services {
    position: absolute; left: 24px; right: 24px; top: 874px;
    list-style: none; display: flex; flex-direction: column; gap: 10px;
  }
  .service-row { display: flex; justify-content: center; align-items: center; gap: 10px; }
  .service {
    display: flex; align-items: center; gap: 7px; white-space: nowrap;
    font-size: 20px; line-height: 28px; color: var(--text); text-transform: uppercase;
  }
  .service + .service::before {
    content: ""; width: 2px; height: 22px; background: #555; margin-right: 10px;
  }
  .tick { width: 20px; height: 20px; flex: none; }
  .contact-bar {
    position: absolute; left: 0; bottom: 0; width: 849px; height: 80px;
    background: var(--charcoal); border-top: 6px solid var(--red);
    display: flex; align-items: center; justify-content: center; gap: 24px;
    font-family: "Oswald", sans-serif; font-weight: 700; font-size: 40px; color: #ffffff;
  }
  .contact-item { display: flex; align-items: center; gap: 12px; }
  .contact-divider { width: 3px; height: 44px; background: #ffffff; }
  .contact-icon { width: 34px; height: 34px; }
</style>
</head>
<body>
<main class="poster">
  <svg class="header-stripes" viewBox="0 0 849 170" aria-hidden="true">
    <path d="M0 120 L230 150 L0 150 Z" fill="var(--red)"/>
    <path d="M0 100 L260 138 L250 146 L0 112 Z" fill="#222"/>
    <path d="M849 120 L619 150 L849 150 Z" fill="var(--red)"/>
    <path d="M849 100 L589 138 L599 146 L849 112 Z" fill="#222"/>
  </svg>

  <div class="brand">
    <span class="brand-dot"></span>
    <span class="brand-name">Ridgeline Mechanical Services</span>
  </div>

  <div class="hero-photo" role="img" aria-label="Row of semi trucks parked on gravel under a blue sky"></div>

  <div class="headline-band"><h1 class="headline">HEAVY DUTY REPAIRS</h1></div>

  <div class="gallery">
    <div class="gallery-photo photo-truck" role="img" aria-label="Semi truck on the road"></div>
    <div class="gallery-photo photo-loader" role="img" aria-label="Backhoe loader on a construction site"></div>
    <div class="gallery-photo photo-tractor" role="img" aria-label="Red tractor working a field"></div>
  </div>

  <h2 class="services-title">OUR SERVICES</h2>

  <svg width="0" height="0" style="position:absolute">
    <symbol id="tick-mark" viewBox="0 0 20 20">
      <circle cx="10" cy="10" r="9" fill="var(--red)"/>
      <path d="M6.5 6.5 L13.5 13.5 M13.5 6.5 L6.5 13.5" stroke="#fff" stroke-width="2.4" stroke-linecap="round"/>
    </symbol>
  </svg>

  <ul class="services">
    <li class="service-row">
      <span class="service"><svg class="tick"><use href="#tick-mark"/></svg>CVIPS</span>
      <span class="service"><svg class="tick"><use href="#tick-mark"/></svg>Welding</span>
      <span class="service"><svg class="tick"><use href="#tick-mark"/></svg>Air Conditioning</span>
      <span class="service"><svg class="tick"><use href="#tick-mark"/></svg>Engine Rebuilds</span>
    </li>
    <li class="service-row">
      <span class="service"><svg class="tick"><use href="#tick-mark"/></svg>Diagnostics</span>
      <span class="service"><svg class="tick"><use href="#tick-mark"/></svg>Fleet Management</span>
      <span class="service"><svg class="tick"><use href="#tick-mark"/></svg>Tire Repair and Sales</span>
    </li>
    <li class="service-row">
      <span class="service"><svg class="tick"><use href="#tick-mark"/></svg>Electrical, Hydraulic &amp; Power Train Repairs</span>
      <span class="service"><svg class="tick"><use href="#tick-mark"/></svg>Part Sales</span>
    </li>
    <li class="service-row">
      <span class="service"><svg class="tick"><use href="#tick-mark"/></svg>Fleet Maintenance</span>
      <span class="service"><svg class="tick"><use href="#tick-mark"/></svg>Deleting and Tuning</span>
      <span class="service"><svg class="tick"><use href="#tick-mark"/></svg>Onsite &amp; Offsite Repairs</span>
    </li>
    <li class="service-row">
      <span class="service"><svg class="tick"><use href="#tick-mark"/></svg>After Market Installs Outfitting</span>
      <span class="service"><svg class="tick"><use href="#tick-mark"/></svg>Warranty Approved</span>
    </li>
    <li class="service-row">
      <span class="service"><svg class="tick"><use href="#tick-mark"/></svg>Full Recertification Overhauling</span>
    </li>
  </ul>

  <footer class="contact-bar">
    <span class="contact-item">
      <svg class="contact-icon" viewBox="0 0 24 24" aria-hidden="true"><path fill="#fff" d="M6.6 10.8a15.1 15.1 0 0 0 6.6 6.6l2.2-2.2a1 1 0 0 1 1-.25 11.4 11.4 0 0 0 3.6.57 1 1 0 0 1 1 1V20a1 1 0 0 1-1 1A17 17 0 0 1 3 4a1 1 0 0 1 1-1h3.5a1 1 0 0 1 1 1c0 1.25.2 2.45.57 3.57a1 1 0 0 1-.25 1z"/></svg>
      780-555-0148
    </span>
    <span class="contact-divider"></span>
    <span class="contact-item">
      <svg class="contact-icon" viewBox="0 0 24 24" aria-hidden="true"><path fill="#fff" d="M12 2a7 7 0 0 0-7 7c0 5.2 7 13 7 13s7-7.8 7-13a7 7 0 0 0-7-7zm0 9.5A2.5 2.5 0 1 1 12 6.5a2.5 2.5 0 0 1 0 5z"/></svg>
      CORRAN, ALBERTA
    </span>
  </footer>
</main>
</body>
</html>
```